Online business manager needs a website

I need a website designed and then coded. I am an online business manager serving a number of different industries providing administrative support to existing small businesses and helping solo practitioners get their new business up and running.

I didn't have a logo formally designed but have been using the attached avatar and wouldn't mind something that incorporated that.

The business doesn't have an official name, so I've just been using my name Lena Pruvost, Online Business Manager or Lena Pruvost, OBM. I've attached two documents that I have made previously for an example of content.

I would prefer the final site be in Wordpress.

Requirements
Must have
• A way to contact me, testimonials, list of services

```html
<!DOCTYPE html>
<html lang="en">
<head>
<meta charset="utf-8">
<title>Lena Pruvost — Online Business Manager</title>
<link rel="stylesheet" href="https://fonts.googleapis.com/css2?family=Outfit:wght@200;300;400;500;600;700&display=swap">
<style>
:root{
  --blue:#3b6ad6;
  --ink:#1d1f26;
  --text:#3c4049;
  --muted:#7b8089;
  --line:#dfe2e7;
  --soft:#f4f5f8;
  --white:#ffffff;
  --grad:linear-gradient(90deg,#3f5ccf,#2bbadb);
}
*{box-sizing:border-box;margin:0;padding:0}
html,body{width:1200px;height:3916px;overflow:hidden}
body{position:relative;background:var(--white);font-family:"Outfit",sans-serif;color:var(--text)}
.abs{position:absolute}
.btn{position:absolute;display:flex;align-items:center;justify-content:center;border-radius:20px;font-size:13px;font-weight:500}
.btn-fill{background:var(--grad);color:var(--white)}
.btn-line{border:1.5px solid var(--blue);color:var(--blue);background:transparent}
.btn-line-white{border:1.5px solid var(--white);color:var(--white)}
.ph{position:absolute}
h2.section-title{position:absolute;left:0;width:1200px;text-align:center;font-size:37px;font-weight:300;color:var(--ink)}
h2.section-title b{font-weight:700}

/* header */
.brand{position:absolute;display:flex;align-items:center;gap:10px}
.brand-avatar{width:56px;height:48px;border-radius:6px;background:linear-gradient(135deg,#f2c94c,#6ea8d8)}
.brand-name{font-size:20px;font-weight:700;letter-spacing:2px;color:var(--blue);line-height:1}
.brand-role{font-size:12.5px;color:var(--muted);margin-top:4px}
.nav{position:absolute;top:30px;left:543px;display:flex;gap:31px;font-size:12.5px;color:var(--ink)}
.nav .on{color:var(--blue);position:relative}
.nav .on::after{content:"";position:absolute;left:50%;bottom:-14px;width:12px;height:2px;margin-left:-6px;background:var(--blue)}
.nav .on-blue{color:var(--white)}
.nav-cta{position:absolute;left:917px;top:22px;width:122px;height:34px;border:1.5px solid var(--white);border-radius:18px;color:var(--white);font-size:13px;display:flex;align-items:center;justify-content:center}

/* hero */
.hello{left:158px;top:166px;font-size:18px;color:var(--ink)}
.hero-name{left:158px;top:194px;font-size:52px;font-weight:700;color:var(--ink);letter-spacing:-.5px;white-space:nowrap}
.hero-name span{font-weight:200}
.hero-role{left:162px;top:270px;font-size:12.5px;letter-spacing:3px;font-weight:500;color:var(--blue)}
.hero-copy{left:161px;top:302px;width:390px;font-size:12px;line-height:24px;color:var(--text)}
.photo-ring{left:621px;top:91px;width:426px;height:426px;border-radius:50%;background:var(--white);padding:7px}
.photo-ring .ph{position:static;width:100%;height:100%;border-radius:50%;background:linear-gradient(160deg,#8b8f95,#d8b07a 55%,#9aa3ad)}

/* about */
.monitor{left:161px;top:651px;width:374px;height:365px}
.about-title{left:608px;top:660px;font-size:37px;font-weight:300;color:var(--ink)}
.about-title b{font-weight:700}
.about-sub{left:612px;top:713px;font-size:12.5px;letter-spacing:2.5px;color:var(--ink)}
.about-copy{left:611px;top:740px;width:430px;font-size:12px;line-height:25.5px}

/* services */
.card{position:absolute;top:1244px;width:203px;height:351px;border:1px solid var(--line);background:var(--white);text-align:center}
.card.lift{border-color:transparent;box-shadow:0 8px 22px rgba(30,40,70,.12)}
.card .ph{position:static;height:142px;width:100%}
.card-icon{position:absolute;left:50%;top:112px;width:60px;height:60px;margin-left:-30px;border-radius:50%;background:var(--grad);border:4px solid var(--white);display:flex;align-items:center;justify-content:center}
.card h3{margin-top:44px;font-size:13.5px;font-weight:600;color:var(--ink);line-height:20px;padding:0 14px}
.card ul{list-style:none;margin-top:6px;font-size:11.5px;line-height:22.5px;color:var(--text);padding:0 12px}

/* work */
.work{left:0;top:1738px;width:1200px;height:627px;background:linear-gradient(160deg,#5c4ec4 0%,#3e7fd6 45%,#27dccd 100%)}
.work h2{position:absolute;top:66px;width:1200px;text-align:center;font-size:37px;font-weight:300;color:var(--white)}
.work h2 b{font-weight:700}
.tile{position:absolute;top:137px;width:277px;height:277px}
.cap{position:absolute;top:440px;width:277px;text-align:center;color:var(--white)}
.cap b{display:block;font-size:14px;font-weight:600}
.cap span{display:block;font-size:12px;margin-top:9px;opacity:.95}
.arrow{position:absolute;width:38px;height:38px;border-radius:50%;display:flex;align-items:center;justify-content:center}

/* partners */
.partners{position:absolute;left:161px;top:2412px;width:880px;display:flex;justify-content:space-between;align-items:center}
.partner{display:flex;align-items:center;gap:8px;font-size:20px;font-weight:600;color:#8a8f99}
.partner i{display:block;width:22px;height:22px;border-radius:50%;background:#8a8f99}
.partner i.sq{border-radius:3px}
.rule{left:161px;top:2487px;width:879px;height:1px;background:var(--line)}

/* testimonials */
.quote{position:absolute;top:2665px;width:428px;height:270px;border:1px solid var(--line);background:var(--white);text-align:center}
.quote.lift{border-color:transparent;box-shadow:0 8px 24px rgba(30,40,70,.10)}
.quote p{margin-top:60px;padding:0 30px;font-size:12px;line-height:25.5px}
.quote h4{margin-top:10px;font-size:12px;letter-spacing:1.5px;font-weight:700;color:var(--ink)}
.quote small{display:block;margin-top:8px;font-size:12px}
.avatar{position:absolute;top:2626px;width:78px;height:78px;border-radius:50%;border:4px solid var(--white);box-shadow:0 0 0 1px var(--line);background:linear-gradient(135deg,#e7b48a,#7cc37c)}
.dots{position:absolute;left:566px;top:2966px;display:flex;gap:13px;align-items:center}
.dots i{display:block;width:6px;height:6px;border-radius:50%;background:#b8c8ef}
.dots i.on{width:9px;height:9px;border:2px solid var(--blue);background:var(--white)}

/* contact */
.contact-bg{left:0;top:3049px;width:1200px;height:582px;background:var(--soft)}
.form-box{left:161px;top:3189px;width:878px;height:365px;background:var(--white);box-shadow:0 4px 20px rgba(30,40,70,.05)}
.field{position:absolute;border-bottom:1px solid var(--line);font-size:11.5px;color:var(--muted);padding-bottom:12px}
.field.active{border-bottom:1.5px solid var(--blue);color:var(--ink)}
.info{left:687px;top:3189px;width:352px;height:365px;background:linear-gradient(160deg,#3b6fd6,#29c3d6)}
.info .brand-name,.info .brand-role{color:var(--white)}
.info-row{position:absolute;left:46px;display:flex;align-items:center;gap:13px;color:var(--white);font-size:13px;font-weight:500}
.info-row i{width:32px;height:32px;border-radius:50%;background:var(--white);display:flex;align-items:center;justify-content:center}

/* footer */
.footer{left:0;top:3631px;width:1200px;height:285px;background:linear-gradient(160deg,#5a4ec6 0%,#3f86d8 45%,#26dccc 100%);color:var(--white)}
.footer .brand-name,.footer .brand-role{color:var(--white)}
.foot-nav{position:absolute;top:164px;left:0;width:1200px;display:flex;justify-content:center;gap:32px;font-size:12.5px}
.foot-nav .on{position:relative}
.foot-nav .on::after{content:"";position:absolute;left:50%;bottom:-12px;width:12px;height:2px;margin-left:-6px;background:var(--white)}
.copy{position:absolute;top:248px;width:1200px;text-align:center;font-size:12px}
</style>
</head>
<body>

<svg class="abs" style="left:0;top:0" width="1200" height="520" aria-hidden="true">
  <defs><linearGradient id="heroGrad" x1="0" y1="0" x2="1" y2="1"><stop offset="0" stop-color="#3e63d2"/><stop offset="1" stop-color="#27c6d6"/></linearGradient></defs>
  <path d="M684 0 Q690 92 760 118 L1200 487 V0 Z" fill="url(#heroGrad)"/>
</svg>

<header>
  <div class="brand" style="left:158px;top:14px">
    <div class="brand-avatar" role="img" aria-label="Illustrated avatar of the business owner at a laptop"></div>
    <div><div class="brand-name">LENA PRUVOST</div><div class="brand-role">Online Business Manager</div></div>
  </div>
  <nav class="nav"><span class="on">Home</span><span>About Me</span><span class="on-blue">What I Do Best</span><span class="on-blue">Client Love</span></nav>
  <div class="nav-cta">Contact Me</div>
</header>

<section class="hero">
  <div class="abs hello">Hello</div>
  <h1 class="abs hero-name"><span>I’m </span>Lena Pruvost</h1>
  <div class="abs hero-role">DIGITAL BUSINESS MANAGER</div>
  <p class="abs hero-copy">Focused on the live event and entertainment industry. Helping artists and owners to better manage their career and business by strategically reviewing systems, recommending operational efficiencies, and managing inboxes.</p>
  <div class="btn btn-fill" style="left:161px;top:422px;width:134px;height:36px">Contact Me</div>
  <div class="abs photo-ring"><div class="ph" role="img" aria-label="Portrait photo of Lena Pruvost outdoors in a city street"></div></div>
</section>

<svg class="abs" style="left:0;top:520px" width="600" height="700" aria-hidden="true">
  <defs><linearGradient id="aboutGrad" x1="0" y1="0" x2="1" y2="1"><stop offset="0" stop-color="#3b66d3"/><stop offset="1" stop-color="#29c8d4"/></linearGradient></defs>
  <polygon points="0,5 520,440 0,695" fill="url(#aboutGrad)"/>
</svg>

<section class="about">
  <div class="ph monitor" role="img" aria-label="Desktop monitor showing a photo of Lena Pruvost in front of pink flowers" style="background:linear-gradient(180deg,#2a2d33 0%,#7a4a6a 35%,#c9497e 62%,#d9dbe0 85%,#c8cbd1 100%);border-radius:10px"></div>
  <h2 class="abs about-title">About <b>Me</b></h2>
  <div class="abs about-sub">LENA PRUVOST, VIRTUAL ASSISTANT</div>
  <p class="abs about-copy">Hi! I’m so excited that you have chosen to explore my portfolio. Helping businesses achieve their goals is my passion, and I’m thrilled that with my assistance you will have more time for your own passion project. I thrive while working independently, which means you can be confident when leaving tasks for me. The type of work that lights me up is anything involving organization and/or spreadsheets. You need data analyzed that includes multiple nested if formulas? You have an overwhelming amount of email to sort through and appointments to book? I’m your gal!</p>
  <div class="btn btn-fill" style="left:612px;top:995px;width:135px;height:36px">Contact Me</div>
</section>

<section class="services">
  <h2 class="section-title" style="top:1170px">What I <b>Do Best</b></h2>

  <div class="card" style="left:161px">
    <div class="ph" role="img" aria-label="Photo of an assistant with a headset at a laptop" style="background:linear-gradient(135deg,#d9dde3,#f3f1ee)"></div>
    <div class="card-icon"><svg width="26" height="26" viewBox="0 0 24 24" fill="none" stroke="#fff" stroke-width="1.6"><path d="M4 14v-2a8 8 0 0 1 16 0v2"/><rect x="3" y="13" width="4" height="6" rx="1"/><rect x="17" y="13" width="4" height="6" rx="1"/></svg></div>
    <h3>Virtual Assistance</h3>
    <ul><li>Calendar Management</li><li>Email Management</li><li>Light Graphic Design</li><li>Data Entry</li></ul>
  </div>

  <div class="card lift" style="left:386px">
    <div class="ph" role="img" aria-label="Photo of a person working on content at a computer" style="background:linear-gradient(135deg,#2b3446,#7d8593 60%,#c9c2b4)"></div>
    <div class="card-icon"><svg width="26" height="26" viewBox="0 0 24 24" fill="none" stroke="#fff" stroke-width="1.6"><rect x="3" y="4" width="18" height="13" rx="1.5"/><path d="M8 21h8M12 17v4M7 9h4M7 12h6"/></svg></div>
    <h3>Social Media &amp; Content Management</h3>
    <ul><li>Content Repurposing</li><li>Graphics Creation</li><li>Audiogram Creation</li><li>Search Engine Optimization</li></ul>
  </div>

  <div class="card" style="left:610px">
    <div class="ph" role="img" aria-label="Photo of colourful charts on a tablet and paper" style="background:linear-gradient(135deg,#dfe6ee,#b9c7d9 50%,#eef1f5)"></div>
    <div class="card-icon"><svg width="26" height="26" viewBox="0 0 24 24" fill="none" stroke="#fff" stroke-width="1.6"><path d="M4 20V10M10 20V6M16 20v-8M22 20H2"/></svg></div>
    <h3>Finance Management</h3>
    <ul><li>Create Invoices</li><li>Track Receivables</li><li>Analyze Expenses</li><li>Year Over Year Analytics</li></ul>
  </div>

  <div class="card" style="left:835px">
    <div class="ph" role="img" aria-label="Photo of two business people reviewing documents" style="background:linear-gradient(135deg,#c9ced6,#4b5260 55%,#e4e6ea)"></div>
    <div class="card-icon"><svg width="26" height="26" viewBox="0 0 24 24" fill="none" stroke="#fff" stroke-width="1.6"><circle cx="12" cy="12" r="3"/><path d="M12 3v3M12 18v3M3 12h3M18 12h3M5.6 5.6l2.1 2.1M16.3 16.3l2.1 2.1M5.6 18.4l2.1-2.1M16.3 7.7l2.1-2.1"/></svg></div>
    <h3>Business Management</h3>
    <ul><li style="line-height:18px;margin:2px 0">Creation of Operating Procedures</li><li>Review of Website Strategy</li><li>Reporting and Analytics</li><li>Project Management</li></ul>
  </div>

  <div class="btn btn-line" style="left:532px;top:1627px;width:136px;height:38px">Contact Me</div>
</section>

<section class="abs work">
  <h2>My <b>Work</b></h2>
  <div class="arrow" style="left:86px;top:258px;border:1.5px solid #fff;background:#fff"><svg width="14" height="14" viewBox="0 0 24 24" fill="none" stroke="#3b6ad6" stroke-width="2.4"><path d="M19 12H5M11 6l-6 6 6 6"/></svg></div>
  <div class="arrow" style="left:1075px;top:258px;border:1.5px solid rgba(255,255,255,.7)"><svg width="14" height="14" viewBox="0 0 24 24" fill="none" stroke="#fff" stroke-width="2.4"><path d="M5 12h14M13 6l6 6-6 6"/></svg></div>

  <div class="ph tile" style="left:161px;background:linear-gradient(135deg,#f6e9df,#f1d6c4)" role="img" aria-label="Podcast promo graphic on owning business workflows and automations with two guest portraits"></div>
  <div class="ph tile" style="left:461px;background:#f55a55" role="img" aria-label="Quote graphic in coral red reading No Need For Full On Glam"></div>
  <div class="ph tile" style="left:761px;background:linear-gradient(135deg,#f4efe9,#e8ddd3);border:5px solid #252a5c" role="img" aria-label="Podcast episode graphic on being mindful with body movement with guest portraits"></div>

  <div class="cap" style="left:161px"><b>Lorem Ipsum Dolor</b><span>Lorem Ipsum is simply dummy text</span></div>
  <div class="cap" style="left:461px"><b>Lorem Ipsum Dolor</b><span>Lorem Ipsum is simply dummy text</span></div>
  <div class="cap" style="left:761px"><b>Lorem Ipsum Dolor</b><span>Lorem Ipsum is simply dummy text</span></div>

  <div class="btn btn-line-white" style="left:521px;top:515px;width:158px;height:36px">View More Work</div>
</section>

<div class="partners">
  <div class="partner"><i></i>Northwind</div>
  <div class="partner"><i class="sq"></i>Brightlane</div>
  <div class="partner"><i></i>Cobalt &amp; Co</div>
  <div class="partner"><i class="sq"></i>Fernhill</div>
  <div class="partner">Atlas Studio</div>
</div>
<div class="abs rule"></div>

<section class="testimonials">
  <h2 class="section-title" style="top:2552px">Client <b>Love</b></h2>
  <div class="arrow" style="left:86px;top:2781px;border:1.5px solid var(--line)"><svg width="14" height="14" viewBox="0 0 24 24" fill="none" stroke="#b9bec7" stroke-width="2.4"><path d="M19 12H5M11 6l-6 6 6 6"/></svg></div>
  <div class="arrow" style="left:1075px;top:2781px;border:1.5px solid var(--blue)"><svg width="14" height="14" viewBox="0 0 24 24" fill="none" stroke="#3b6ad6" stroke-width="2.4"><path d="M5 12h14M13 6l6 6-6 6"/></svg></div>

  <div class="quote lift" style="left:161px">
    <p>“When it became apparent that a project would take more time than I had, Lena stepped up to take on the required research. She was thorough and timely; able to meet a last-minute 12-hour deadline. I would highly recommend Lena to assist with your next project.”</p>
    <h4>- MAREN D. HOLT</h4><small>Ridgeway Home Works</small>
  </div>
  <div class="quote" style="left:611px">
    <p>“When it became apparent that a project would take more time than I had, Lena stepped up to take on the required research. She was thorough and timely; able to meet a last-minute 12-hour deadline. I would highly recommend Lena to assist with your next project.”</p>
    <h4>- MAREN D. HOLT</h4><small>Ridgeway Home Works</small>
  </div>
  <div class="ph avatar" style="left:336px" role="img" aria-label="Client portrait photo"></div>
  <div class="ph avatar" style="left:786px" role="img" aria-label="Client portrait photo"></div>
  <div class="dots"><i></i><i class="on"></i><i></i><i></i></div>
</section>

<section class="contact">
  <div class="abs contact-bg"></div>
  <h2 class="section-title" style="top:3113px">Get In <b>Touch</b></h2>
  <div class="abs form-box">
    <div class="field active" style="left:53px;top:55px;width:203px">Noémie |</div>
    <div class="field" style="left:278px;top:55px;width:204px">Last Name</div>
    <div class="field" style="left:53px;top:115px;width:203px">Email Address</div>
    <div class="field" style="left:278px;top:115px;width:204px">Phone Number</div>
    <div class="field" style="left:53px;top:176px;width:429px;height:76px">Message</div>
    <div class="btn btn-line" style="left:53px;top:277px;width:150px;height:38px">Send Message</div>
  </div>
  <div class="abs info">
    <div class="brand" style="left:46px;top:56px">
      <div class="brand-avatar" role="img" aria-label="Illustrated avatar of the business owner at a laptop"></div>
      <div><div class="brand-name">LENA PRUVOST</div><div class="brand-role">Online Business Manager</div></div>
    </div>
    <div class="info-row" style="top:140px"><i><svg width="14" height="14" viewBox="0 0 24 24" fill="none" stroke="#3b6ad6" stroke-width="2.2"><rect x="7" y="2" width="10" height="20" rx="2"/><path d="M11 18h2"/></svg></i>555.318.2046</div>
    <div class="info-row" style="top:185px"><i><svg width="14" height="14" viewBox="0 0 24 24" fill="none" stroke="#3b6ad6" stroke-width="2.2"><rect x="3" y="5" width="18" height="14" rx="2"/><path d="M3 7l9 6 9-6"/></svg></i>hello@lenapruvost.example</div>
    <div class="info-row" style="top:230px"><i></i>Lena Pruvost</div>
    <div class="info-row" style="top:275px"><i></i>/LenaPruvostOBM</div>
  </div>
</section>

<footer class="abs footer">
  <div class="brand" style="left:478px;top:70px">
    <div class="brand-avatar" role="img" aria-label="Illustrated avatar of the business owner at a laptop"></div>
    <div><div class="brand-name">LENA PRUVOST</div><div class="brand-role">Online Business Manager</div></div>
  </div>
  <nav class="foot-nav"><span class="on">Home</span><span>About Me</span><span>What I Do Best</span><span>Client Love</span><span>Contact Me</span></nav>
  <div class="copy">© 2023 Lena Pruvost. All Rights Reserved.</div>
</footer>

</body>
</html>
```